Tova Brisk Fitness Coaching Project

I am a personal trainer based in London. My services include one-on-one PT sessions, bootcamps.
I would like the design to be minimalistic. With light colours: white, pink, purple.
I specialise in weight loss, flexibility, mobility.

Tova Penrick
Personal Trainer
Email: tova.penrick@mailgrove.net
tel: 07500 918 243
Instagram: Tova Brisk

Target Market(s)

adults, mostly females (age 18-50).

Industry/Entity Type

Fitness

Contact Information for Business Card

Tova Penrick
Personal Trainer
tel: 07500 918 243
Instagram: Tova Brisk

Font styles to use
Serif

Colors
eea4c8
fbd4d5
fdf9cf
cfeae6
cee9f5

Requirements
Nice to have
• minimalistic style
• easy to read and remember

```html
<!DOCTYPE html>
<html lang="en">
<head>
<meta charset="utf-8">
<title>Tova Penrick – Personal Trainer Business Card</title>
<link rel="stylesheet" href="https://fonts.googleapis.com/css2?family=Montserrat:wght@400;700&family=Open+Sans:wght@400&display=swap">
<style>
  :root {
    --page-bg: #ececec;
    --front-pink: #e46fae;
    --front-pink-soft: #ec9dc6;
    --front-lilac: #cdbfe6;
    --front-sky: #b9cdee;
    --back-charcoal: #434446;
    --back-charcoal-deep: #3a3b3d;
    --photo-warm: #c9a58a;
    --photo-light: #efe4d6;
    --photo-green: #4f5a3f;
    --text-white: #ffffff;
    --text-white-soft: rgba(255, 255, 255, 0.72);
  }
  * { box-sizing: border-box; margin: 0; padding: 0; }
  html, body {
    width: 1200px;
    height: 719px;
    overflow: hidden;
    background: var(--page-bg);
  }
  .canvas {
    position: relative;
    width: 1200px;
    height: 719px;
  }
  .card {
    position: absolute;
    top: 219px;
    width: 500px;
    height: 280px;
    overflow: hidden;
    box-shadow: 0 6px 22px rgba(0, 0, 0, 0.12);
  }

  /* Front face */
  .card--front {
    left: 70px;
    background: linear-gradient(90deg, var(--front-pink) 0%, var(--front-pink-soft) 40%, var(--front-lilac) 75%, var(--front-sky) 100%);
  }
  .card--front .portrait {
    position: absolute;
    right: 0;
    top: 0;
    width: 58%;
    height: 100%;
    background:
      radial-gradient(ellipse 45% 55% at 55% 40%, rgba(240, 220, 230, 0.75), rgba(240, 220, 230, 0) 70%),
      linear-gradient(90deg, rgba(236, 157, 198, 0) 0%, rgba(214, 196, 232, 0.6) 45%, rgba(196, 214, 240, 0.7) 100%);
  }
  .card--front .name {
    position: absolute;
    left: 95px;
    top: 136px;
    font-family: "Montserrat", sans-serif;
    font-weight: 700;
    font-size: 44px;
    letter-spacing: 0.5px;
    color: rgba(255, 255, 255, 0.82);
  }
  .card--front .role {
    position: absolute;
    left: 95px;
    top: 203px;
    font-family: "Montserrat", sans-serif;
    font-weight: 400;
    font-size: 23px;
    letter-spacing: 0.5px;
    color: var(--text-white-soft);
  }
  .card--front .role .dot { font-size: 14px; vertical-align: middle; margin: 0 10px 0 0; }
  .card--front .role .dot:last-child { margin: 0 0 0 10px; }

  /* Back face */
  .card--back {
    left: 630px;
    background: linear-gradient(90deg, var(--back-charcoal) 0%, var(--back-charcoal) 45%, var(--back-charcoal-deep) 100%);
  }
  .card--back .portrait {
    position: absolute;
    right: 0;
    top: 0;
    width: 46%;
    height: 100%;
    background:
      radial-gradient(ellipse 40% 50% at 60% 35%, var(--photo-light), rgba(239, 228, 214, 0) 75%),
      radial-gradient(ellipse 60% 70% at 70% 55%, var(--photo-warm), rgba(201, 165, 138, 0) 80%),
      linear-gradient(90deg, rgba(67, 68, 70, 0) 0%, var(--photo-green) 45%, #6b6152 100%);
  }
  .card--back .details {
    position: absolute;
    left: 58px;
    top: 110px;
    color: var(--text-white);
  }
  .card--back .name {
    font-family: "Montserrat", sans-serif;
    font-weight: 700;
    font-size: 28px;
    letter-spacing: 0.5px;
  }
  .card--back .role {
    margin-top: 14px;
    font-family: "Montserrat", sans-serif;
    font-size: 13px;
    letter-spacing: 0.4px;
  }
  .contact-list {
    list-style: none;
    margin-top: 14px;
    font-family: "Open Sans", sans-serif;
    font-size: 16px;
  }
  .contact-list li {
    display: flex;
    align-items: center;
    gap: 14px;
    height: 27px;
  }
  .contact-list svg { width: 16px; height: 16px; flex: none; }
  .contact-list .square-mark {
    width: 13px;
    height: 13px;
    margin: 0 1px 0 2px;
    background: var(--text-white);
    border-radius: 2px;
    flex: none;
  }
</style>
</head>
<body>
<main class="canvas">

  <section class="card card--front" aria-label="Business card front">
    <div class="portrait" role="img" aria-label="Portrait photograph of the trainer, softly blended into pink and lilac"></div>
    <h1 class="name">TOVA PENRICK</h1>
    <p class="role"><span class="dot">•</span>PERSONAL TRAINER<span class="dot">•</span></p>
  </section>

  <section class="card card--back" aria-label="Business card back">
    <div class="portrait" role="img" aria-label="Sunlit portrait photograph of the trainer outdoors"></div>
    <div class="details">
      <h2 class="name">TOVA PENRICK</h2>
      <p class="role">PERSONAL TRAINER</p>
      <ul class="contact-list">
        <li>
          <svg viewBox="0 0 16 16" aria-hidden="true"><path fill="#fff" d="M1 6c0-2 3-3 7-3s7 1 7 3v1h-4V5.5H5V7H1z M3 8h10l1 6H2z"/><circle cx="8" cy="11" r="1.6" fill="#434446"/></svg>
          <span>07500 918 243</span>
        </li>
        <li>
          <svg viewBox="0 0 16 16" aria-hidden="true"><rect x="1" y="3" width="14" height="10" rx="1" fill="#fff"/><path d="M1.5 4 8 9l6.5-5" stroke="#434446" stroke-width="1.4" fill="none"/></svg>
          <span>tova.penrick@mailgrove.net</span>
        </li>
        <li>
          <span class="square-mark" aria-hidden="true"></span>
          <span>Tova Brisk</span>
        </li>
      </ul>
    </div>
  </section>

</main>
</body>
</html>
```